Vell Partners Building Business Cards

We need a business card that reflects our business as "Solar Experts" in San Diego. Browse our website www.vellpartners.example our License needs to be displayed as "CSLB# 4718392" our phone number is (619) 555-0147

Save thousands on your electric bills and increase the value of your home while helping to protect the environment. Our solar installation experts will help you design the system that's right for you, using only the highest quality equipment that will look great and give you ideal performance. Our goal is to make you energy independent, and get your electric bill to 0.

Tobias Wrenfield
(619) 555-0147
tobias@vellpartners.example

Target Market(s)

Home owners in san diego looking for solar

Industry/Entity Type

Solar Energy

Contact Information for Business Card

Tobias Wrenfield
(619) 555-0147
tobias@vellpartners.example

Font styles to use
Other font styles liked:
• Use our logo font

Requirements
Must have
• License needs to be displayed as "CSLB# 4718392" our phone number is (619) 555-0147
Nice to have
• Real images of rooftop home solar in san diego
Should not have
• our business address

```html
<!DOCTYPE html>
<html lang="en">
<head>
<meta charset="utf-8">
<title>Vell Partners Building – Business Cards</title>
<link rel="stylesheet" href="https://fonts.googleapis.com/css2?family=Open+Sans:wght@400;600;700&display=swap">
<style>
  :root {
    --navy: #1f4a8c;
    --sun: #fbb021;
    --ink: #2b2b2b;
    --card: #ffffff;
    --backdrop: #ebebeb;
    --art-top: #fcd27a;
    --art-bottom: #8fa6c9;
  }
  * { margin: 0; padding: 0; box-sizing: border-box; }
  html, body { width: 1200px; height: 786px; overflow: hidden; }
  body {
    background: var(--backdrop);
    font-family: "Open Sans", Arial, sans-serif;
    position: relative;
  }
  .card {
    position: absolute;
    top: 250px;
    width: 487px;
    height: 276px;
    background: var(--card);
    overflow: hidden;
    box-shadow: 0 2px 6px rgba(0,0,0,.25);
  }
  .card--front { left: 122px; }
  .card--back  { left: 617px; width: 486px; }

  .wordmark {
    position: absolute;
    color: var(--navy);
    font-weight: 700;
    font-size: 20px;
    line-height: 1.05;
    letter-spacing: -0.3px;
    white-space: nowrap;
  }
  .card--front .wordmark { left: 36px; top: 42px; }
  .card--back  .wordmark { left: 284px; top: 194px; }

  .holder {
    position: absolute;
    left: 36px;
    top: 122px;
    font-size: 16.5px;
    font-weight: 600;
    letter-spacing: 0.6px;
    text-transform: uppercase;
    padding-bottom: 2px;
    border-bottom: 2px solid var(--navy);
    white-space: nowrap;
  }
  .holder__first { color: var(--navy); }
  .holder__last  { color: var(--sun); }

  .contact-list {
    position: absolute;
    left: 36px;
    top: 164px;
    list-style: none;
    font-size: 12px;
    color: var(--ink);
  }
  .contact-list li {
    display: flex;
    align-items: center;
    height: 18.5px;
    white-space: nowrap;
  }
  .contact-list svg {
    width: 12px; height: 12px;
    margin-right: 12px;
    stroke: var(--navy);
    fill: none;
    stroke-width: 1.3;
    flex: none;
  }
  .license {
    position: absolute;
    left: 38px;
    top: 237px;
    font-size: 11.5px;
    font-weight: 600;
    color: var(--navy);
    letter-spacing: 0.8px;
    white-space: nowrap;
  }

  .artwork-area {
    position: absolute;
    top: 0;
    height: 100%;
    background: linear-gradient(180deg, var(--art-top) 0%, var(--art-bottom) 100%);
  }
  .card--front .artwork-area { left: 300px; width: 187px; }
  .card--back  .artwork-area { left: 0; width: 200px; }
</style>
</head>
<body>

  <section class="card card--front" aria-label="Business card front">
    <div class="wordmark">Vell Partners<br>Building</div>

    <div class="holder"><span class="holder__first">Tobias</span> <span class="holder__last">Wrenfield</span></div>

    <ul class="contact-list">
      <li>
        <svg viewBox="0 0 12 12" aria-hidden="true"><path d="M2.5 1h2l1 2.5-1.3 1a6 6 0 0 0 3.3 3.3l1-1.3 2.5 1v2a1 1 0 0 1-1 1A9 9 0 0 1 1.5 2a1 1 0 0 1 1-1z"/></svg>
        (619) 555-0147
      </li>
      <li>
        <svg viewBox="0 0 12 12" aria-hidden="true"><rect x="0.8" y="2.3" width="10.4" height="7.4"/><path d="M0.8 2.3 6 6.6l5.2-4.3M0.8 9.7l3.8-4M11.2 9.7l-3.8-4"/></svg>
        tobias@vellpartners.example
      </li>
      <li>
        <svg viewBox="0 0 12 12" aria-hidden="true"><circle cx="6" cy="6" r="5"/><ellipse cx="6" cy="6" rx="2.2" ry="5"/><path d="M1 6h10M2 3.3h8M2 8.7h8"/></svg>
        www.vellpartners.example
      </li>
    </ul>

    <div class="license">LICENSE-"CSLB# 4718392"</div>

    <div class="artwork-area" role="img" aria-label="Brand artwork area, left half"></div>
  </section>

  <section class="card card--back" aria-label="Business card back">
    <div class="artwork-area" role="img" aria-label="Brand artwork area, right half"></div>
    <div class="wordmark">Vell Partners<br>Building</div>
  </section>

</body>
</html>
```